Bref créative
Business Card for Education Consulting Company
Brio Study Mentors
Simple
Marcus Delavine
President
317 Hollins Court NE
Washington DC 20019
Marcus@briostudymentors-example.com
www.briostudymentors-example.com
Looking for a simple, clean and professional business card. The logo already has the name of the company so there is no need to include again unless you feel it adds to the overall look of the card.
Here is the compnay's logo

```html
<!DOCTYPE html>
<html lang="en">
<head>
<meta charset="utf-8">
<title>Brio Study Mentors – Business Card</title>
<link href="https://fonts.googleapis.com/css2?family=Cinzel:wght@400;600&display=swap" rel="stylesheet">
<style>
  :root {
    --backdrop: #e9e7e3;
    --card-white: #ffffff;
    --card-grey: #585c60;
    --accent-blue: #1f4aa8;
    --brand-navy: #1c3f8f;
    --text-light: #f1f1f1;
    --text-muted: #d6d8da;
    --icon-bg: #e8e8e8;
  }
  * { margin: 0; padding: 0; box-sizing: border-box; }
  html, body {
    width: 1200px; height: 900px; overflow: hidden;
    background: var(--backdrop);
    font-family: "Cinzel", serif;
  }
  .stage {
    width: 1200px; height: 900px;
    display: flex; align-items: center; justify-content: center;
  }
  .business-card {
    position: relative;
    width: 1000px; height: 572px;
    background: var(--card-grey);
    box-shadow: 0 14px 40px rgba(0,0,0,0.22);
    overflow: hidden;
  }
  .card-top {
    position: absolute; left: 0; top: 0;
    width: 100%; height: 250px;
    background: var(--card-white);
  }
  .accent-rule {
    position: absolute; left: 0; top: 250px;
    width: 100%; height: 9px;
    background: var(--accent-blue);
  }
  .brand {
    position: absolute; left: 52px; top: 96px;
    display: flex; align-items: center; gap: 16px;
  }
  .brand-dot {
    width: 40px; height: 40px; border-radius: 50%;
    background: var(--brand-navy);
  }
  .brand-name {
    font-size: 40px; font-weight: 600;
    color: var(--brand-navy);
    letter-spacing: 1px;
  }
  .person {
    position: absolute; right: 60px; top: 300px;
    text-align: right; color: var(--text-light);
  }
  .person-name { font-size: 34px; font-weight: 400; letter-spacing: 1px; }
  .person-title { font-size: 22px; margin-top: 8px; color: var(--text-muted); }
  .contact-list {
    position: absolute; left: 36px; top: 402px;
    list-style: none; color: var(--text-light);
    font-size: 19px; line-height: 30px;
  }
  .contact-list li { display: flex; align-items: center; gap: 12px; }
  .contact-list .continued { padding-left: 34px; }
  .contact-icon { width: 22px; height: 22px; flex: none; }
</style>
</head>
<body>
<main class="stage">
  <section class="business-card">
    <div class="card-top"></div>
    <div class="accent-rule"></div>

    <div class="brand">
      <span class="brand-dot"></span>
      <span class="brand-name">Brio Study Mentors</span>
    </div>

    <div class="person">
      <p class="person-name">Marcus Delavine</p>
      <p class="person-title">President</p>
    </div>

    <ul class="contact-list">
      <li>
        <svg class="contact-icon" viewBox="0 0 22 22" aria-hidden="true">
          <circle cx="11" cy="11" r="11" fill="var(--icon-bg)"/>
          <path d="M5 11 L11 5.5 L17 11 H15 V16 H7 V11 Z" fill="var(--card-grey)"/>
        </svg>
        317 Hollins Court NE
      </li>
      <li class="continued">Washington DC 20019</li>
      <li>
        <svg class="contact-icon" viewBox="0 0 22 22" aria-hidden="true">
          <circle cx="11" cy="11" r="11" fill="var(--icon-bg)"/>
          <path d="M7.5 5.5 L9.5 5.5 L10.5 8.5 L9 9.5 Q10.5 12.5 12.5 13 L13.5 11.5 L16.5 12.5 L16.5 14.5 Q15 16.5 12 15.5 Q7 13.5 6 8.5 Q6 6.5 7.5 5.5 Z" fill="var(--card-grey)"/>
        </svg>
        703-555-0148
      </li>
      <li>
        <svg class="contact-icon" viewBox="0 0 22 22" aria-hidden="true">
          <circle cx="11" cy="11" r="11" fill="var(--icon-bg)"/>
          <rect x="5.5" y="7" width="11" height="8" fill="none" stroke="var(--card-grey)" stroke-width="1.5"/>
          <path d="M5.5 7 L11 11.5 L16.5 7" fill="none" stroke="var(--card-grey)" stroke-width="1.5"/>
        </svg>
        Marcus@briostudymentors-example.com
      </li>
      <li>
        <svg class="contact-icon" viewBox="0 0 22 22" aria-hidden="true">
          <circle cx="11" cy="11" r="11" fill="var(--icon-bg)"/>
          <path d="M6 11 H16 M12.5 7.5 L16 11 L12.5 14.5" fill="none" stroke="var(--card-grey)" stroke-width="1.8"/>
        </svg>
        www.briostudymentors-example.com
      </li>
    </ul>
  </section>
</main>
</body>
</html>
```